Harborpoint Meridian Insurance Services

we are a high end insurance agency we specialize on Auto | Home | Business | Life looking for something professional and luxuries at the same time. if you guys need anything else please let me know.

Auto | Home | Business | Life must be under logo on the back with black background.

i want the back part to be black with our gold logo on it.

Target Market(s)

Auto | Home | Business | Life

Industry/Entity Type

Insurance Broker

Contact Information for Business Card

My logo is gold so a black in the back would be nice.

Font styles to use
Serif

Colors
000000

Requirements
Must have
• Big logo on the back with black background.

```html
<!DOCTYPE html>
<html lang="en">
<head>
<meta charset="utf-8">
<title>Harborpoint Meridian Insurance Services – Business Card</title>
<link href="https://fonts.googleapis.com/css2?family=Cinzel:wght@600&family=Roboto+Slab:wght@700&family=Open+Sans:wght@400&display=swap" rel="stylesheet">
<style>
  :root {
    --ink: #000000;
    --ink-soft: #111111;
    --gold: #ffc414;
    --gold-deep: #f5b000;
    --grey: #9a9a9a;
    --light: #e6e6e6;
    --stage: #dcdcdc;
  }
  * { box-sizing: border-box; margin: 0; padding: 0; }
  html, body { width: 1200px; height: 1000px; overflow: hidden; }
  body {
    background: var(--stage);
    position: relative;
    font-family: "Open Sans", sans-serif;
  }
  .card {
    position: absolute;
    width: 560px;
    height: 320px;
    border-radius: 22px;
    overflow: hidden;
    box-shadow: 0 10px 24px rgba(0,0,0,0.18);
  }
  .card-back { left: 90px; top: 110px; background: var(--ink); }
  .card-front { left: 550px; top: 570px; background: var(--gold); }
  .card svg.bg { position: absolute; inset: 0; width: 100%; height: 100%; }

  .brand {
    position: absolute;
    display: flex;
    align-items: center;
    gap: 14px;
  }
  .brand-mark {
    width: 18px; height: 18px; border-radius: 50%;
    flex: none;
  }
  .brand-name {
    font-family: "Cinzel", serif;
    font-weight: 600;
    font-size: 21px;
    line-height: 1.2;
    letter-spacing: 0.5px;
  }
  .card-back .brand { left: 70px; top: 92px; width: 440px; }
  .card-back .brand-mark { background: var(--gold); }
  .card-back .brand-name { color: var(--gold); }
  .services {
    position: absolute;
    left: 102px; top: 152px;
    font-family: "Cinzel", serif;
    font-weight: 600;
    font-size: 13px;
    letter-spacing: 2px;
    color: var(--grey);
  }
  .services .sep { color: var(--gold); padding: 0 4px; }

  .card-front .brand { left: 60px; top: 62px; width: 440px; }
  .card-front .brand-mark { background: var(--ink-soft); }
  .card-front .brand-name { color: var(--ink-soft); }

  .holder {
    position: absolute;
    left: 60px; top: 192px;
    font-family: "Roboto Slab", serif;
    font-weight: 700;
    font-size: 17px;
    letter-spacing: 1px;
    color: #ffffff;
    text-transform: uppercase;
  }
  .holder .surname { color: var(--gold); }
  .contacts {
    position: absolute;
    left: 60px; top: 222px;
    list-style: none;
    font-size: 13px;
    color: var(--light);
  }
  .contacts li { display: flex; align-items: center; gap: 10px; height: 21px; }
  .contacts svg { width: 12px; height: 12px; fill: var(--gold); flex: none; }
  .contacts .accent { color: var(--gold); }

  .address {
    position: absolute;
    right: 40px; top: 148px;
    text-align: right;
    font-size: 12px;
    line-height: 1.5;
    color: var(--light);
  }
  .address svg { display: block; margin: 0 0 4px auto; width: 12px; height: 14px; fill: var(--gold); }
</style>
</head>
<body>

  <section class="card card-back" aria-label="Card back">
    <svg class="bg" viewBox="0 0 560 320" preserveAspectRatio="none" aria-hidden="true">
      <path d="M0 250 C160 280 330 230 440 150 C500 110 540 100 560 100 L560 320 L0 320 Z" fill="var(--gold)"/>
      <path d="M0 262 C170 292 340 240 450 160 C505 122 540 116 560 118 L560 320 L0 320 Z" fill="var(--ink)"/>
      <path d="M0 300 C180 300 360 250 470 185 C515 160 545 150 560 150 L560 320 L0 320 Z" fill="var(--gold)"/>
    </svg>
    <div class="brand">
      <span class="brand-mark"></span>
      <span class="brand-name">Harborpoint Meridian Insurance Services</span>
    </div>
    <p class="services">Auto<span class="sep">|</span>Home<span class="sep">|</span>Business<span class="sep">|</span>Life</p>
  </section>

  <section class="card card-front" aria-label="Card front">
    <svg class="bg" viewBox="0 0 560 320" preserveAspectRatio="none" aria-hidden="true">
      <path d="M0 150 C60 200 140 200 260 160 C380 120 470 90 560 110 L560 320 L0 320 Z" fill="var(--ink)"/>
      <path d="M0 300 C120 290 260 300 380 320 L0 320 Z" fill="var(--gold-deep)"/>
    </svg>
    <div class="brand">
      <span class="brand-mark"></span>
      <span class="brand-name">Harborpoint Meridian Insurance Services</span>
    </div>

    <p class="holder">Daniel <span class="surname">Hale</span></p>
    <ul class="contacts">
      <li><svg viewBox="0 0 24 24"><path d="M6.6 10.8a15.1 15.1 0 0 0 6.6 6.6l2.2-2.2c.3-.3.7-.4 1-.2 1.1.4 2.3.6 3.6.6.6 0 1 .4 1 1V20c0 .6-.4 1-1 1A17 17 0 0 1 3 4c0-.6.4-1 1-1h3.5c.6 0 1 .4 1 1 0 1.3.2 2.5.6 3.6.1.3 0 .7-.2 1z"/></svg>+000 123 456 789</li>
      <li><svg viewBox="0 0 24 24"><path d="M2 5h20v14H2z M2 5l10 8 10-8" stroke="#000" stroke-width="1.5"/></svg>yourname@email.com</li>
      <li><svg viewBox="0 0 24 24"><circle cx="12" cy="12" r="10"/></svg><span>www.<span class="accent">yoursitename</span>.com</span></li>
    </ul>

    <p class="address">
      <svg viewBox="0 0 24 28"><path d="M12 0a9 9 0 0 0-9 9c0 7 9 19 9 19s9-12 9-19a9 9 0 0 0-9-9zm0 12.5A3.5 3.5 0 1 1 12 5.5a3.5 3.5 0 0 1 0 7z"/></svg>
      Your Street Address,<br>Harborview, 1234
    </p>
  </section>

</body>
</html>
```